Landing page for B2B Product Idea Validation Event

We need a single landing page design for the world’s first competition to help aspiring entrepreneurs to validate their new business 2 business (B2B) web application ideas.

We like the following landing pages as examples for the structure and sectioning we would like to see for this landing page:
http://ny.brelvox-summit.com/
https://kiv.com/kivfest

There should be around 5 sections including an application form.

Target Market(s)

Entrepreneurs

Industry/Entity Type

Business Software

Number of Pages Required

1 page

Font styles to use
Serif

Requirements
Must have
• Colors must be similar to the logo provided.

```html
<!DOCTYPE html>
<html lang="en">
<head>
<meta charset="utf-8">
<title>Tradeforge – B2B Idea Validation</title>
<link href="https://fonts.googleapis.com/css2?family=Montserrat:wght@400;600;700;800&family=Open+Sans:ital,wght@0,400;0,600;0,700;1,400&display=swap" rel="stylesheet">
<style>
:root{
  --blue:#1b8fd0;
  --blue-dark:#0f6fa8;
  --ink:#222;
  --text:#555;
  --muted:#888;
  --navy:#0e2236;
  --grey-bg:#efefef;
  --footer:#2b2b2b;
  --footer-bottom:#1f1f1f;
  --newsletter:#3c93d6;
  --white:#fff;
}
*{margin:0;padding:0;box-sizing:border-box}
html,body{width:1200px;height:2880px;overflow:hidden;background:var(--white)}
body{position:relative;font-family:'Open Sans',sans-serif;color:var(--text)}
.abs{position:absolute}
h1,h2,h3,h4,.brand{font-family:'Montserrat',sans-serif}

/* header */
.site-header{position:absolute;left:0;top:0;width:1200px;height:130px;border-top:4px solid var(--blue);background:var(--white)}
.brand{position:absolute;left:86px;top:24px;font-size:34px;font-weight:700;color:var(--ink);letter-spacing:1px}
.contact-top{position:absolute;right:72px;top:30px;display:flex;align-items:center;gap:6px;font-size:15px;color:var(--ink);font-weight:600}
.dot{width:28px;height:28px;border-radius:50%;background:var(--blue);display:inline-block}
.dot.alt{background:#e9534f;border-radius:6px;margin-left:8px;margin-right:4px}
.nav{position:absolute;right:60px;top:78px;display:flex;font-size:15px;color:var(--ink)}
.nav a{padding:7px 24px;text-decoration:none;color:var(--ink);border-left:1px solid #ddd}
.nav a:first-child{border:none;background:var(--blue);color:var(--white);margin-right:18px;padding:7px 22px}

/* hero */
.hero{position:absolute;left:0;top:130px;width:1200px;height:513px;background:linear-gradient(100deg,#5a6470 0%,#3d4650 45%,#2b3440 100%)}
.hero-photo{position:absolute;inset:0;background:radial-gradient(ellipse at 30% 55%,rgba(200,205,210,.35),transparent 60%)}
.hero-mark{position:absolute;left:712px;top:42px;font-family:'Montserrat',sans-serif;font-size:44px;font-weight:800;color:#111}
.hero-kicker{position:absolute;left:574px;top:194px;font-size:12px;font-weight:700;color:var(--white);font-family:'Montserrat',sans-serif;white-space:nowrap}
.hero-sub{position:absolute;left:574px;top:212px;font-size:25px;color:var(--white);font-family:'Montserrat',sans-serif;white-space:nowrap}
.hero-title{position:absolute;left:572px;top:238px;font-size:48px;font-weight:800;color:var(--white);font-family:'Montserrat',sans-serif;white-space:nowrap}
.hero-arrow{position:absolute;top:230px}

/* section titles */
.section-title{position:absolute;left:0;width:1200px;text-align:center;font-size:32px;font-weight:600;color:var(--ink);letter-spacing:.5px}
.section-title span{display:inline-block;padding:0 4px 8px;border-bottom:2px solid currentColor}

/* welcome */
.intro{position:absolute;left:130px;top:752px;width:940px;text-align:center;font-size:12.5px;line-height:24px}
.video{position:absolute;left:95px;top:826px;width:462px;height:290px}
.video-screen{position:absolute;left:50px;top:0;width:362px;height:275px;border:12px solid #111;border-radius:10px;background:linear-gradient(180deg,#3a2a1a,#c88838 55%,#4a2c12)}
.video-base{position:absolute;left:0;top:270px;width:462px;height:14px;background:#222;border-radius:0 0 40px 40px}
.play{position:absolute;left:220px;top:120px;width:36px;height:26px;background:#e52d27;border-radius:6px}
.play:after{content:"";position:absolute;left:14px;top:7px;border-left:10px solid #fff;border-top:6px solid transparent;border-bottom:6px solid transparent}
.about{position:absolute;left:622px;top:832px;width:430px}
.about h3{font-size:20px;line-height:24px;font-weight:400;color:var(--ink);margin-bottom:10px}
.about p{font-size:12.5px;line-height:22px;margin-bottom:8px}
.btn{position:absolute;left:622px;top:1068px;width:165px;height:46px;background:var(--blue);color:var(--white);font-size:14px;display:flex;align-items:center;justify-content:center;border-radius:2px}

/* services */
.services{position:absolute;left:0;top:1200px;width:1200px;height:373px;background:linear-gradient(135deg,#12304a,#0b1e30 60%,#15314a)}
.services .section-title{top:30px;color:var(--white)}
.service{position:absolute;top:116px;width:240px;text-align:center;color:var(--white)}
.service .icon{width:96px;height:96px;margin:0 auto 18px;border-radius:50%;background:var(--blue);display:flex;align-items:center;justify-content:center}
.service.active .icon{box-shadow:0 0 0 4px rgba(27,143,208,.4)}
.service h4{font-size:13.5px;font-weight:700;margin-bottom:6px}
.service p{font-size:12.5px;line-height:23px;color:#d8e2ea;padding:0 10px}

/* speakers */
.speaker{position:absolute;top:1712px;width:240px;text-align:center}
.avatar{width:160px;height:160px;margin:0 auto;border-radius:50%;border:5px solid #e6e6e6;background:linear-gradient(180deg,#e9eef3,#9aa7b4);box-shadow:0 6px 10px rgba(0,0,0,.12)}
.speaker h4{margin-top:20px;font-size:17px;font-weight:400;color:var(--ink)}
.speaker .role{font-size:11px;color:var(--ink)}
.speaker p{font-size:12.5px;line-height:22px;margin-top:4px}
.socials{display:flex;gap:8px;justify-content:center;margin-top:18px}
.socials i{width:36px;height:36px;border-radius:50%;border:1px solid #ccc;display:block}

/* testimonials & events */
.band-grey{position:absolute;left:0;top:2098px;width:1200px;height:398px;background:var(--grey-bg)}
.col-title{position:absolute;top:2144px;font-size:26px;font-weight:600;color:var(--ink)}
.quote{position:absolute;left:86px;top:2200px;width:434px;height:110px;background:#f7f7f7;border:1px solid #ddd;padding:18px 36px;font-style:italic;font-size:12px;line-height:22px;color:var(--muted)}
.client{position:absolute;left:86px;top:2336px;width:86px;height:86px;border-radius:50%;border:4px solid #fff;background:linear-gradient(180deg,#dde3e8,#8b98a5)}
.client-name{position:absolute;left:208px;top:2366px;font-size:11px;font-weight:700;color:var(--blue)}
.client-role{position:absolute;left:208px;top:2385px;font-size:11px;color:var(--ink)}
.pager{position:absolute;left:490px;top:2388px;display:flex;gap:4px}
.pager i{width:12px;height:12px;border-radius:50%;background:#bbb;display:block}
.event{position:absolute;left:572px;width:540px}
.event .thumb{position:absolute;left:0;top:0;width:112px;height:100px;border:4px solid #fff;background:linear-gradient(135deg,#3b4a5a,#9aa4ae)}
.event h4{position:absolute;left:138px;top:0;font-size:13px;font-weight:700;color:var(--ink)}
.event .date{position:absolute;left:138px;top:24px;font-size:11px;color:var(--blue)}
.event p{position:absolute;left:138px;top:46px;width:400px;font-size:12px;line-height:22px}
.rule{position:absolute;left:572px;top:2316px;width:512px;height:1px;background:#d4d4d4}

/* newsletter */
.newsletter{position:absolute;left:0;top:2496px;width:1200px;height:72px;background:var(--newsletter);color:var(--white)}
.nl-icon{position:absolute;left:84px;top:14px;width:44px;height:44px;border-radius:50%;border:2px solid #fff;display:flex;align-items:center;justify-content:center}
.nl-title{position:absolute;left:180px;top:20px;font-size:28px;font-family:'Montserrat',sans-serif}
.nl-input{position:absolute;left:512px;top:16px;width:438px;height:42px;background:#fff;color:#999;font-size:13px;padding:11px 14px}
.nl-btn{position:absolute;left:974px;top:16px;width:132px;height:42px;background:#333;font-size:15px;display:flex;align-items:center;justify-content:center}

/* footer */
.footer{position:absolute;left:0;top:2568px;width:1200px;height:264px;background:var(--footer);color:#ccc}
.f-title{position:absolute;top:30px;font-size:18px;color:#fff;border-bottom:1px solid #888;padding-bottom:4px;font-family:'Montserrat',sans-serif}
.f-links{position:absolute;left:86px;top:76px;list-style:none;font-size:12px;line-height:31px}
.f-links li:before{content:"›";margin-right:8px}
.map{position:absolute;left:288px;top:76px;width:240px;height:152px;border:4px solid #ddd;background:linear-gradient(135deg,#ece3c6,#f5efd8 50%,#d9d3b5)}
.f-info{position:absolute;left:560px;font-size:12px;line-height:20px;display:flex;gap:14px}
.f-brand{position:absolute;left:864px;top:130px;font-size:26px;font-weight:600;color:#fff;font-family:'Montserrat',sans-serif}
.footer-bottom{position:absolute;left:0;top:2832px;width:1200px;height:48px;background:var(--footer-bottom);font-size:12px;color:#bbb}
.footer-bottom .copy{position:absolute;left:86px;top:16px}
.footer-bottom .socials{position:absolute;right:86px;top:6px;margin:0}
.footer-bottom .socials i{width:34px;height:34px;border:none;background:#3a78c3}
</style>
</head>
<body>

<header class="site-header">
  <div class="brand">Tradeforge</div>
  <div class="contact-top">
    <span class="dot"></span><span class="dot"></span><span class="dot"></span><span class="dot"></span>
    <span class="dot alt"></span>(555)-310-2740
  </div>
  <nav class="nav"><a>Home</a><a>About us</a><a>Services</a><a>Solutions</a><a>Options</a></nav>
</header>

<section class="hero" role="img" aria-label="Business team in a meeting room watching a presentation, with network graphics overlay">
  <div class="hero-photo"></div>
  <div class="hero-mark">Tradeforge</div>
  <div class="hero-kicker">WORLD'S FIRST COMPETITION TO HELP ASPIRING ENTREPRENEURS TO VALIDATE THEIR</div>
  <div class="hero-sub">NEW BUSINESS 2 BUSINESS (B2B) IDEAS</div>
  <div class="hero-title">START DIFFERENTLY</div>
  <svg class="hero-arrow" style="left:28px" width="22" height="60"><path d="M18 4 L4 30 L18 56" stroke="#fff" stroke-width="2" fill="none" opacity=".7"/></svg>
  <svg class="hero-arrow" style="right:28px" width="22" height="60"><path d="M4 4 L18 30 L4 56" stroke="#fff" stroke-width="2" fill="none" opacity=".7"/></svg>
</section>

<h2 class="section-title" style="top:682px"><span>WELCOME TO TRADEFORGE</span></h2>
<p class="intro">Lorem Ipsum is simply dummy text of the printing and typesetting industry. Lorem Ipsum has been the industry's standard dummy text ever since the 1500s, when an unknown printer took a galley of type and scrambled it to make a type specimen book.</p>
<div class="video">
  <div class="video-screen" role="img" aria-label="Video still of business people silhouetted against a bright window"></div>
  <div class="play"></div>
  <div class="video-base"></div>
</div>
<div class="about">
  <h3>Finibus Bonorum et Malorum</h3>
  <p>Lorem Ipsum is simply dummy text of the printing and typesetting industry. Lorem Ipsum has been the industry's standard dummy text ever since the 1500s, when an unknown printer took a galley of type and scrambled it to make a type specimen book. It has survived not only five centuries, but also the leap into electronic typesetting, remaining essentially unchanged.</p>
  <p>It was popularised in the 1960s with the release of Letraset sheets containing Lorem Ipsum passages</p>
</div>
<div class="btn">View more info</div>

<section class="services">
  <h2 class="section-title"><span>OUR SERVICES</span></h2>
  <div class="service" style="left:130px"><div class="icon"><svg width="40" height="40" viewBox="0 0 40 40" fill="none" stroke="#fff" stroke-width="3"><circle cx="18" cy="18" r="13"/><circle cx="18" cy="18" r="6"/><path d="M22 22 L34 34"/></svg></div><h4>WHY ARE WE BUILDING THIS?</h4><p>Lorem Ipsum is simply dummy text of the printing and typesetting industry Lorem Ipsum</p></div>
  <div class="service active" style="left:380px"><div class="icon"><svg width="40" height="36" viewBox="0 0 40 36" fill="#fff"><rect x="2" y="2" width="36" height="24" rx="2"/><rect x="14" y="28" width="12" height="3"/><rect x="10" y="31" width="20" height="3"/></svg></div><h4>WHAT ARE WE BUILDING ?</h4><p>Lorem Ipsum is simply dummy text of the printing and typesetting industry Lorem Ipsum</p></div>
  <div class="service" style="left:630px"><div class="icon"><svg width="40" height="36" viewBox="0 0 40 36" fill="#fff"><rect x="15" y="2" width="10" height="9"/><rect x="2" y="25" width="10" height="9"/><rect x="15" y="25" width="10" height="9"/><rect x="28" y="25" width="10" height="9"/><path d="M20 11v14M7 25v-6h26v6" stroke="#fff" stroke-width="2" fill="none"/></svg></div><h4>HOW ARE WE BUILDING?</h4><p>Lorem Ipsum is simply dummy text of the printing and typesetting industry Lorem Ipsum</p></div>
  <div class="service" style="left:880px"><div class="icon"><svg width="30" height="40" viewBox="0 0 30 40" fill="none" stroke="#fff" stroke-width="2.5"><path d="M15 3a11 11 0 0 0-6 20v6h12v-6A11 11 0 0 0 15 3z"/><path d="M10 34h10M12 38h6"/></svg></div><h4>NAVIGATE BACK ON TRACK</h4><p>Lorem Ipsum is simply dummy text of the printing and typesetting industry the industry's standard</p></div>
</section>

<h2 class="section-title" style="top:1630px"><span>SPEAKERS</span></h2>
<div class="speaker" style="left:114px"><div class="avatar" role="img" aria-label="Portrait of speaker Daniel Morrow"></div><h4>DANIEL MORROW</h4><div class="role">CEO</div><p>Lorem Ipsum is simply dummy text of the printing and typesetting industry.</p><div class="socials"><i></i><i></i><i></i></div></div>
<div class="speaker" style="left:358px"><div class="avatar" role="img" aria-label="Portrait of speaker Clara Whitfield"></div><h4>CLARA WHITFIELD</h4><div class="role">CEO</div><p>Lorem Ipsum is simply dummy text of the printing and typesetting industry.</p><div class="socials"><i></i><i></i><i></i></div></div>
<div class="speaker" style="left:613px"><div class="avatar" role="img" aria-label="Portrait of speaker Owen Pryce"></div><h4>OWEN PRYCE</h4><div class="role">CEO</div><p>Lorem Ipsum is simply dummy text of the printing and typesetting industry.</p><div class="socials"><i></i><i></i><i></i></div></div>
<div class="speaker" style="left:862px"><div class="avatar" role="img" aria-label="Portrait of speaker Marcus Hale"></div><h4>MARCUS HALE</h4><div class="role">CEO</div><p>Lorem Ipsum is simply dummy text of the printing and typesetting industry.</p><div class="socials"><i></i><i></i><i></i></div></div>

<div class="band-grey"></div>
<h3 class="col-title" style="left:86px">OUR TESTIMONIALS</h3>
<h3 class="col-title" style="left:572px">LATEST EVENTS</h3>
<blockquote class="quote">Sed ut perspiciatis unde omnis iste natus error sit voluptatem accusantium doloremque laudantium, totam rem aperiam, eaque ipsa quae ab illo inventore veritatis et quasi architecto...</blockquote>
<div class="client" role="img" aria-label="Portrait of client Evan Tolliver"></div>
<div class="client-name">EVAN TOLLIVER</div>
<div class="client-role">Business man</div>
<div class="pager"><i></i><i></i></div>

<article class="event" style="top:2190px">
  <div class="thumb" role="img" aria-label="Event image of a digital business graphic"></div>
  <h4>WE STRIVE TO DETERMINE THE NEEDS OF EVERY</h4>
  <div class="date">▣ 23/11/2016</div>
  <p>Lorem Ipsum is simply dummy text of the printing and typesetting industry. Lorem Ipsum has been the industry's...</p>
</article>
<div class="rule"></div>
<article class="event" style="top:2332px">
  <div class="thumb" role="img" aria-label="Event image of a tablet showing charts" style="background:linear-gradient(135deg,#dfe4ea,#8e9aa6)"></div>
  <h4>FIND OUT ABOUT OUR SERVICES, OUR METHODS</h4>
  <div class="date">▣ 23/11/2016</div>
  <p>Lorem Ipsum is simply dummy text of the printing and typesetting industry. Lorem Ipsum has been the industry's...</p>
</article>

<section class="newsletter">
  <div class="nl-icon"><svg width="20" height="14" viewBox="0 0 20 14"><rect width="20" height="14" rx="2" fill="#fff"/><path d="M1 1 L10 8 L19 1" stroke="#3c93d6" stroke-width="1.5" fill="none"/></svg></div>
  <div class="nl-title">Newsletter Signup</div>
  <svg class="abs" style="left:452px;top:14px" width="20" height="44"><path d="M3 2 L17 22 L3 42" stroke="#fff" stroke-width="1.5" fill="none" opacity=".7"/></svg>
  <div class="nl-input">Enter your email address...</div>
  <div class="nl-btn">Sign Up</div>
</section>

<footer class="footer">
  <div class="f-title" style="left:86px">Quick Links</div>
  <ul class="f-links"><li>Home</li><li>About us</li><li>Services</li><li>Solutions</li><li>Options</li></ul>
  <div class="f-title" style="left:284px">Contact details</div>
  <div class="map" role="img" aria-label="Street map showing the office location"></div>
  <div class="f-info" style="top:76px"><svg width="12" height="16" viewBox="0 0 12 16"><path d="M6 0a6 6 0 0 0-6 6c0 4 6 10 6 10s6-6 6-10a6 6 0 0 0-6-6z" fill="#ddd"/><circle cx="6" cy="6" r="2" fill="#2b2b2b"/></svg><div>Tradeforge<br>8820 Larkspur Avenue Suite 410<br>Fairhaven, VA 20190-4400.</div></div>
  <div class="f-info" style="top:148px;font-size:14px"><svg width="14" height="14" viewBox="0 0 14 14"><path d="M3 0l3 3-2 2a8 8 0 0 0 5 5l2-2 3 3-2 3C6 14 0 8 0 2z" fill="#ddd"/></svg><div>(555)-310-2740</div></div>
  <div class="f-info" style="top:200px"><svg width="14" height="11" viewBox="0 0 14 11"><rect width="14" height="11" rx="1" fill="#ddd"/><path d="M1 1l6 5 6-5" stroke="#2b2b2b" fill="none"/></svg><div>info@tradeforge.example</div></div>
  <div class="f-brand">Corvane Labs</div>
</footer>
<div class="footer-bottom">
  <div class="copy">© 2016 Tradeforge. All right reserved</div>
  <div class="socials"><i></i><i></i><i></i><i style="background:#e8922a"></i></div>
</div>

</body>
</html>
```